Hotdogs & Burgers restaurant needs a new menu design

We need a new menu design for our restaurant "Pupvella". Pupvella is a fast food specialized in hotdogs and burgers.We are looking for a simple easy menu design that walk through our customer to order the sandwich ==> the fries =>> the sides and the drinks. Pupvella Menu:* Sandwiches**Hotdogs Our special fresh grilled hotdog served on fresh buns (Regular – 1.300 OMR / Franks – 2.000 OMR)*** DoganzaLettuce, tomato, jalapeno, pickle, onion, corn, chips, cheese, ketchup, mayo, mustard*** PepperBell pepper, onion, sweet chili sauce, avocado*** Chili FlamesChili carne, cheddar cheese, honey mustard*** ChicagoTomato, pickle, red onion, sweet relish, mustard*** New YorkGrilled onion, beef bacon, barbecue sauce, chili mustard*** Egg & CheeseOmelet, cheese, ketchup, mayo, mustard** Burgers 100% all natural beef & freshly ground, 100 grams each patty served on fresh buns.(Single patty - 2.000 OMR / double patty - 2.500 OMR)*** Sweet Beef BurgerBeef bacon, cheese, lettuce, tomato, pickle.*** Cheese Beef BurgerCheese, pickle, Pupvella sauce.*** Mexican Beef BurgerGuacamole sauce, red onion, lettuce, tomato, Pupvella sauce.*** Chicken BurgerFried chicken patty, lettuce, tomato, ranch sauce, Pupvella sauce== ToppingsExtra veggies 0.100 OMRExtra cheese 0.200 OMRExtra beef Bacon 0.400 OMRExtra patty 0.500 OMR*Fries**Regular 0.600 OMR**Crispy 0.800 OMR**Wedges 0.800 OMR**Chili fries 1.500 OMRTopped with our chili carne, cheddar cheese, jalapeno, honey mustard**Lava fries 1.500 OMRTopped with fried bacon, fried onion, cheddar cheese, ranch sauce*Sides**Crispy strips 1.800 OMR5 pieces of chicken strips topped with BBQ sauce or honey mustard sauce, Pupvella side sauce**Jalapeno cheese balls 1.300 OMR6 pieces of jalapeno cheese balls, sweet chili side sauce**Nachos 1.500 OMRA plate of nachos topped with cheddar cheese and jalapeno*Drinks**Flavored sparkling cans 0.800 OMR **Fresh orange juice 1.400 OMR**Mineral water 0.300 OMR**Soft drink 0.400 OMR**Mojito 1.500 OMRThe menu should not have any of our products pictures (icons/symbols proffered). we would prefer if the designs have unique icons/symbols created for Pupvella. you can check our Picturo page https://www.picturo-app.example/pupvella.official/

Industry/Entity Type

American Restaurant

Colors

Designer to choose colors to be used in the design.

Requirements
Must have
• Pupvella Logo, Icons

```html
<!DOCTYPE html>
<html lang="en">
<head>
<meta charset="utf-8">
<title>Pupvella Menu</title>
<link rel="stylesheet" href="https://fonts.googleapis.com/css2?family=Rammetto+One&family=Overlock:ital,wght@0,700;0,900;1,400&display=swap">
<style>
  :root {
    --hazard-yellow: #e5b820;
    --hazard-dark: #2a2410;
    --board-dark: #1c1c1c;
    --board-mid: #2e2e2e;
    --heading-yellow: #f5d31a;
    --text-light: #f0f0f0;
    --illus-cream: #d9d2bc;
    --illus-warm: #b5653a;
    --illus-green: #4e7a2c;
    --illus-glass: #c9c48a;
    --illus-cup: #d8dce6;
    --social-blue: #3b5a9a;
  }
  html, body {
    margin: 0;
    padding: 0;
    width: 848px;
    height: 1200px;
    overflow: hidden;
    background: var(--board-dark);
  }
  .canvas {
    position: relative;
    width: 840px;
    height: 1188px;
    transform: scale(1.0095);
    transform-origin: 0 0;
    font-family: "Overlock", sans-serif;
    color: var(--text-light);
  }
  .hazard-frame {
    position: absolute;
    inset: 0;
    background: linear-gradient(135deg, var(--hazard-yellow), #b88d12 45%, var(--hazard-yellow) 70%, var(--hazard-dark));
  }
  .board {
    position: absolute;
    left: 38px;
    top: 40px;
    width: 767px;
    height: 1115px;
    background: radial-gradient(ellipse at 50% 40%, var(--board-mid), var(--board-dark) 75%);
  }
  .abs { position: absolute; margin: 0; white-space: nowrap; }
  .section-title {
    font-family: "Rammetto One", sans-serif;
    font-size: 20px;
    color: var(--heading-yellow);
    line-height: 1;
  }
  .item-name {
    font-family: "Overlock", sans-serif;
    font-weight: 900;
    font-size: 14.5px;
    line-height: 1;
  }
  .desc {
    font-style: italic;
    font-size: 13.5px;
    line-height: 19px;
  }
  .price {
    font-style: italic;
    font-size: 15.5px;
    line-height: 20.5px;
  }
  .bullet::before {
    content: "▲ ";
    font-size: 9px;
    font-style: normal;
    vertical-align: 2px;
  }
  .illustration { position: absolute; border-radius: 14px; }
  .illus-sandwich { left: 330px; top: 135px; width: 80px; height: 85px; background: linear-gradient(160deg, var(--illus-cream), #9d9277); }
  .illus-steak { left: 680px; top: 130px; width: 92px; height: 80px; background: linear-gradient(160deg, var(--illus-green), var(--illus-warm)); }
  .illus-hotdog { left: 395px; top: 375px; width: 60px; height: 70px; background: linear-gradient(160deg, #c94030, #d9a560); }
  .illus-fries { left: 660px; top: 290px; width: 112px; height: 105px; background: linear-gradient(180deg, #e3c253, var(--illus-green)); }
  .illus-omelette { left: 385px; top: 555px; width: 78px; height: 72px; background: linear-gradient(160deg, #e6d089, #c0653f); }
  .illus-strips { left: 672px; top: 525px; width: 105px; height: 62px; background: linear-gradient(160deg, #f0ede6, #e09a3a); }
  .illus-burger { left: 385px; top: 665px; width: 86px; height: 118px; background: linear-gradient(180deg, #c5883e, #6d4a2a 55%, #c5883e); }
  .illus-bottle { left: 372px; top: 850px; width: 62px; height: 82px; background: linear-gradient(180deg, #8a6a3a, var(--illus-glass)); }
  .illus-drinks { left: 680px; top: 855px; width: 92px; height: 110px; background: linear-gradient(150deg, var(--illus-cup), #e0a840); }
  .illus-logo-sausage { left: 430px; top: 950px; width: 120px; height: 80px; background: linear-gradient(135deg, #8a2020, #5a1414); border-radius: 40px; }
  .social-links {
    position: absolute;
    left: 106px;
    top: 1080px;
    display: flex;
    gap: 12px;
  }
  .social-link {
    display: flex;
    align-items: center;
    gap: 5px;
    color: var(--text-light);
    text-decoration: none;
    font-weight: 700;
    font-size: 12.5px;
  }
  .social-link .mark {
    width: 14px;
    height: 14px;
    background: var(--social-blue);
  }
  .brand-name {
    position: absolute;
    left: 375px;
    top: 1030px;
    width: 370px;
    text-align: center;
    font-family: "Rammetto One", sans-serif;
    font-size: 58px;
    line-height: 1;
    color: var(--heading-yellow);
    margin: 0;
  }
</style>
</head>
<body>
<main class="canvas">
  <div class="hazard-frame" role="img" aria-label="Yellow and black hazard stripe border"></div>
  <div class="board" role="img" aria-label="Dark scratched chalkboard texture"></div>

  <!-- Left column: sandwiches -->
  <h2 class="abs section-title" style="left:106px;top:108px;">Sandwiches</h2>
  <h3 class="abs item-name" style="left:106px;top:139px;">Hotdogs</h3>
  <p class="abs desc" style="left:106px;top:154px;">Our special fresh grilled hotdog<br>served on fresh buns</p>
  <p class="abs price" style="left:106px;top:192px;">Regular – 1.300 OMR<br>Franks – 2.000 OMR)</p>

  <h3 class="abs item-name" style="left:106px;top:259px;">Pupvella</h3>
  <p class="abs desc" style="left:106px;top:274px;">Lettuce, tomato, jalapeno, pickle, onion,<br>corn, chips, cheese, ketchup, mayo, mustard</p>

  <h3 class="abs item-name" style="left:106px;top:336px;">Pepper</h3>
  <p class="abs desc" style="left:106px;top:351px;">Bell pepper, onion, sweet chili sauce, avocado</p>

  <h3 class="abs item-name" style="left:106px;top:395px;">Chili Flames</h3>
  <p class="abs desc" style="left:106px;top:410px;">Chili carne, cheddar cheese, honey mustard</p>

  <h3 class="abs item-name" style="left:106px;top:454px;">Chicago</h3>
  <p class="abs desc" style="left:106px;top:469px;">Tomato, pickle, red onion, sweet relish, mustard</p>

  <h3 class="abs item-name" style="left:106px;top:512px;">New York</h3>
  <p class="abs desc" style="left:106px;top:528px;">Grilled onion, beef bacon, barbecue sauce,<br>chili mustard</p>

  <h3 class="abs item-name" style="left:106px;top:591px;">Egg &amp; Cheese</h3>
  <p class="abs desc" style="left:106px;top:606px;">Omelet, cheese, ketchup, mayo, mustard</p>

  <h2 class="abs section-title" style="left:106px;top:652px;">Burgers</h2>
  <p class="abs desc" style="left:106px;top:675px;">100% all natural beef &amp; freshly ground,<br>100 grams each patty served on fresh buns.</p>
  <p class="abs price" style="left:106px;top:713px;">Single patty - 2.000 OMR<br>Double patty - 2.500 OMR</p>

  <h3 class="abs item-name" style="left:106px;top:780px;">Sweet Beef Burger</h3>
  <p class="abs desc" style="left:106px;top:795px;">Beef bacon, cheese, lettuce, tomato, pickle.</p>

  <h3 class="abs item-name" style="left:106px;top:838px;">Cheese Beef Burger</h3>
  <p class="abs desc" style="left:106px;top:853px;">Cheese, pickle, Pupvella sauce.</p>

  <h3 class="abs item-name" style="left:106px;top:897px;">Mexican Beef Burger</h3>
  <p class="abs desc" style="left:106px;top:912px;">Guacamole sauce, red onion, lettuce,<br>tomato, Pupvella sauce.</p>

  <h3 class="abs item-name" style="left:106px;top:975px;">Chicken Burger</h3>
  <p class="abs desc" style="left:106px;top:990px;">Fried chicken patty, lettuce, tomato,<br>ranch sauce, Pupvella sauce</p>

  <nav class="social-links">
    <a class="social-link" href="#"><span class="mark"></span>Friendloop</a>
    <a class="social-link" href="#"><span class="mark"></span>Chirply</a>
    <a class="social-link" href="https://www.picturo-app.example/pupvella.official/"><span class="mark"></span>Picturo</a>
  </nav>

  <!-- Right column -->
  <h2 class="abs section-title" style="left:485px;top:173px;">Toppings</h2>
  <p class="abs price" style="left:485px;top:198px;">Extra Veggies 0.100 OMR<br>Extra Cheese 0.200 OMR<br>Extra Beef Bacon 0.400 OMR<br>Extra Patty 0.500 OMR</p>

  <h2 class="abs section-title" style="left:485px;top:307px;">Fries</h2>
  <p class="abs desc" style="left:485px;top:331px;">
    <span class="bullet">Regular 0.600 OMR</span><br>
    <span class="bullet">Crispy 0.800 OMR</span><br>
    <span class="bullet">Wedges 0.800 OMR</span><br>
    &nbsp;&nbsp;&nbsp;Chili fries 1.500 OMR<br>
    &nbsp;&nbsp;&nbsp;Topped with our chili carne,<br>
    &nbsp;&nbsp;&nbsp;cheddar cheese, jalapeno,<br>
    &nbsp;&nbsp;&nbsp;honey mustard<br>
    <span class="bullet">Lava fries 1.500 OMR</span><br>
    &nbsp;&nbsp;Topped with fried bacon, fried onion,<br>
    &nbsp;&nbsp;&nbsp;cheddar cheese, ranch sauce
  </p>

  <h2 class="abs section-title" style="left:485px;top:543px;">Sides</h2>
  <p class="abs desc" style="left:485px;top:568px;">
    <span class="bullet">&nbsp;Crispy strips 1.800 OMR</span><br>
    5 pieces of chicken strips topped with<br>
    BBQ sauce or honey mustard sauce,<br>
    Pupvella side sauce<br>
    <span class="bullet">&nbsp;Jalapeno cheese balls 1.300 OMR</span><br>
    <br>
    &nbsp;6 pieces of jalapeno cheese balls,<br>
    &nbsp;sweet chili side sauce<br>
    <span class="bullet">Nachos 1.500 OMR</span><br>
    A plate of nachos topped with cheddar<br>
    cheese and jalapeno
  </p>

  <h2 class="abs section-title" style="left:485px;top:798px;">Drinks</h2>
  <p class="abs desc" style="left:485px;top:823px;">
    <span class="bullet">Flavored sparkling cans 0.800 OMR</span><br>
    <span class="bullet">Fresh orange juice 1.400 OMR</span><br>
    <span class="bullet">Mineral water 0.300 OMR</span><br>
    <span class="bullet">Soft drink 0.400 OMR</span><br>
    <span class="bullet">Mojito 1.500 OMR</span>
  </p>

  <!-- Illustrations -->
  <div class="illustration illus-sandwich" role="img" aria-label="Hand-drawn sandwich with label"></div>
  <div class="illustration illus-steak" role="img" aria-label="Hand-drawn beef steak with label"></div>
  <div class="illustration illus-hotdog" role="img" aria-label="Hand-drawn hotdog with label"></div>
  <div class="illustration illus-fries" role="img" aria-label="Hand-drawn french fries box with label"></div>
  <div class="illustration illus-omelette" role="img" aria-label="Hand-drawn omelette wrap with label"></div>
  <div class="illustration illus-strips" role="img" aria-label="Hand-drawn plate of chicken strips with label"></div>
  <div class="illustration illus-burger" role="img" aria-label="Hand-drawn burgers with label"></div>
  <div class="illustration illus-bottle" role="img" aria-label="Hand-drawn sauce bottle"></div>
  <div class="illustration illus-drinks" role="img" aria-label="Hand-drawn cup and drink can with label"></div>
  <div class="illustration illus-logo-sausage" role="img" aria-label="Sausage on a fork decoration"></div>

  <p class="brand-name">Pupvella</p>
</main>
</body>
</html>
```